Biz Card Design BTPW

New business card for a new company.
Logo was completed by a designer on ArtFlock and looking to continue requesting additional services.
Company Name: Bright Tidal Power Works
Although this company is starting in Canada, we will be moving towards a global presence within the next 6 months.
Key elements to this business are as follows.
Energy Procurement
Energy Reduction Services
Demand Side Consulting
Energy Efficiency Consulting
Saving Clients Money
Helping Them Go "Green"
Managing Their Energy Requirements
Basically the goal for our company is to find the best procurement solution for our clients and reduce their energy consumption. This reduces their expenses and the amount of greenhouse gas they produce on a daily basis.
I have been in the energy footprint for the last 20 years and know that most companies are looking to "do whatever is necessary to get them to sign on the dotted line". I would prefer to walk away from a client that I can't help than to put them into a situation that they will regret for years to come. This is where the "BRIGHT" part of the company name comes from.
The following is a catch phrase that encompasses what we do.
"Reducing your carbon footprint & energy bill at the same time!"
The back of the card needs to have this statement along with some sort of illustration. The back is a playground for creative ideas.
The front of the card needs the following.
Logo.
First & Last Name (Ned Varsolo)
Title (Energy Warrior)
Phone Number (555) 314-2769
Fax Number (555) 871-4420
Email Address ned@brighttidalpowerworks.example
Address 47 elmwick ave Toronto Ontario K2K 2K2
I want it to be a card that is remembered when any of my staff give it to a customer. It HAS to stand out.
Target Market(s)
Business Owners, Decision Makers, 30 to 65+
Industry/Entity Type
Business
Look and feel
Each slider illustrates characteristics of the customer's brand and the style your logo design should communicate.

```html
<!DOCTYPE html>
<html lang="en">
<head>
<meta charset="utf-8">
<title>BTPW Business Card</title>
<link rel="stylesheet" href="https://fonts.googleapis.com/css2?family=Montserrat:wght@400;600;700&family=Open+Sans:ital,wght@1,400&family=Libre+Baskerville:ital@1&display=swap">
<style>
  :root {
    --page: #ffffff;
    --card-line: #bdbdbd;
    --brand-blue: #3a67b1;
    --brand-green: #3daa48;
    --back-blue: #3d6fb8;
    --back-green: #22b04b;
    --ink-label: #222222;
    --white: #ffffff;
  }
  html, body {
    margin: 0;
    padding: 0;
    overflow: hidden;
    background: var(--page);
  }
  .sheet {
    position: relative;
    width: 1200px;
    height: 900px;
    background: var(--page);
    font-family: "Montserrat", sans-serif;
  }
  .card {
    position: absolute;
    overflow: hidden;
    box-sizing: border-box;
  }
  .card--front {
    left: 366px; top: 140px;
    width: 430px; height: 260px;
    border: 1px solid var(--card-line);
    border-top-right-radius: 60px;
    background: var(--white);
  }
  .brand {
    position: absolute;
    left: 120px; top: 80px;
    display: flex;
    align-items: center;
    gap: 8px;
  }
  .brand__dot {
    width: 14px; height: 14px;
    border-radius: 50%;
    background: var(--brand-green);
  }
  .brand__name {
    font-weight: 700;
    font-size: 19px;
    color: var(--brand-blue);
    letter-spacing: -0.2px;
    white-space: nowrap;
  }
  .contact {
    position: absolute;
    left: 30px; top: 170px;
  }
  .contact__name {
    margin: 0;
    font-weight: 700;
    font-size: 17px;
    letter-spacing: 1.6px;
    color: var(--brand-blue);
  }
  .contact__title {
    margin: 2px 0 12px;
    font-weight: 700;
    font-size: 8.5px;
    letter-spacing: 0.8px;
    color: var(--brand-green);
  }
  .contact__line {
    margin: 0 0 5px;
    font-size: 8.5px;
    color: var(--brand-green);
    white-space: nowrap;
  }
  .card--back {
    top: 544px;
    width: 454px; height: 264px;
    border-top-left-radius: 60px;
  }
  .card--blue { left: 44px; background: var(--back-blue); }
  .card--green { left: 714px; background: var(--back-green); }
  .card__globe {
    position: absolute;
    left: -40px; top: -60px;
    width: 380px; height: 380px;
    border-radius: 50%;
    background: radial-gradient(circle, rgba(255,255,255,0.14), rgba(255,255,255,0.06) 70%, rgba(255,255,255,0) 72%);
  }
  .tagline {
    position: absolute;
    right: 32px; top: 104px;
    margin: 0;
    font-family: "Open Sans", sans-serif;
    font-style: italic;
    font-size: 17px;
    line-height: 28px;
    text-align: right;
    color: var(--white);
  }
  .tagline__accent { color: var(--back-blue); }
  .back-mark {
    position: absolute;
    right: 16px; bottom: 14px;
    font-weight: 700;
    font-size: 12px;
    color: var(--white);
  }
  .divider-word {
    position: absolute;
    left: 590px; top: 658px;
    font-family: "Open Sans", sans-serif;
    font-style: italic;
    font-size: 20px;
    color: var(--ink-label);
  }
  .side-label {
    position: absolute;
    font-family: "Libre Baskerville", serif;
    font-style: italic;
    font-size: 13px;
    letter-spacing: 2px;
    color: var(--ink-label);
  }
</style>
</head>
<body>
<main class="sheet">
  <section class="card card--front" aria-label="Card front">
    <div class="brand">
      <span class="brand__dot"></span>
      <span class="brand__name">Bright Tidal Power Works</span>
    </div>
    <div class="contact">
      <p class="contact__name">NED VARSOLO</p>
      <p class="contact__title">ENERGY WARRIOR</p>
      <p class="contact__line">47 elmwick ave Toronto Ontario K2K 2K2</p>
      <p class="contact__line">P (555) 314-2769 &nbsp; F (555) 871-4420 &nbsp; | ned@brighttidalpowerworks.example</p>
    </div>
  </section>
  <span class="side-label" style="left:370px; top:414px;">front</span>

  <section class="card card--back card--blue" aria-label="Card back, blue version">
    <div class="card__globe" role="img" aria-label="Faint globe graphic"></div>
    <p class="tagline">Reducing your carbon footprint<br>&amp; energy bill at the same time!</p>
    <span class="back-mark">BTPW</span>
  </section>

  <span class="divider-word">or</span>

  <section class="card card--back card--green" aria-label="Card back, green version">
    <div class="card__globe" role="img" aria-label="Faint globe graphic"></div>
    <p class="tagline">Reducing <span class="tagline__accent">your carbon footprint<br>&amp; energy bill at the same time!</span></p>
    <span class="back-mark">BTPW</span>
  </section>

  <span class="side-label" style="left:48px; top:816px;">back</span>
  <span class="side-label" style="left:722px; top:816px;">back</span>
</main>
</body>
</html>
```